Automotive lighting company needs professional business card

Hello, we are an automotive lighting company and looking to have a professional business card designed for us. We have included some images which can be used on the card. Website is www.brightlanemotorparts.example which has all of our details on it. Email is brightlanemotorparts@mailbox.example phone number is 1300 862 317 thank you guys!

Target Market(s)

Automotive industry

Contact Information for Business Card

Phone - 1300 862 317
Web - www.brightlanemotorparts.example
Email - brightlanemotorparts@mailbox.example

Requirements
Must have
• Looking to have a dark theme. Elegant and professional. Needs to look and feel like a high quality card to represent high quality company.

```html
<!DOCTYPE html>
<html lang="en">
<head>
<meta charset="utf-8">
<title>Brightlane Motor Parts – Business Card</title>
<link href="https://fonts.googleapis.com/css2?family=Michroma&family=Arimo:wght@400&display=swap" rel="stylesheet">
<style>
  :root {
    --backdrop: #1c1c1e;
    --metal-light: #b9babc;
    --metal-mid: #a4a5a8;
    --metal-dark: #8e8f92;
    --accent-blue: #1d8fd1;
    --ink-dark: #2a2b2e;
    --emboss: #9a9b9e;
  }
  * { box-sizing: border-box; margin: 0; padding: 0; }
  html, body { width: 1200px; height: 800px; overflow: hidden; }
  body {
    background: var(--backdrop);
    display: flex;
    align-items: center;
    justify-content: center;
    gap: 40px;
  }
  .card {
    width: 300px;
    height: 490px;
    background: linear-gradient(160deg, var(--metal-light) 0%, var(--metal-mid) 55%, var(--metal-dark) 100%);
    box-shadow: 0 18px 40px rgba(0,0,0,0.6);
    position: relative;
  }
  .card--contact {
    text-align: center;
    padding-top: 62px;
  }
  .person-name {
    font-family: "Michroma", sans-serif;
    font-size: 17px;
    color: var(--accent-blue);
    letter-spacing: 0.5px;
  }
  .person-role {
    font-family: "Michroma", sans-serif;
    font-size: 10px;
    color: var(--ink-dark);
    margin-top: 4px;
  }
  .contact-list {
    list-style: none;
    margin-top: 26px;
    font-family: "Arimo", sans-serif;
    font-size: 11px;
    line-height: 1.5;
    color: var(--ink-dark);
  }
  .contact-list .phone { font-size: 13px; margin-bottom: 4px; }
  .emboss-area {
    position: absolute;
    left: 60px;
    top: 250px;
    width: 180px;
    height: 180px;
    border-radius: 50%;
    background: radial-gradient(circle, var(--emboss) 0%, rgba(154,155,158,0) 70%);
  }
  .card--brand {
    display: flex;
    align-items: center;
    justify-content: center;
  }
  .brand {
    display: flex;
    align-items: center;
    gap: 10px;
  }
  .brand-dot {
    width: 14px;
    height: 14px;
    border-radius: 50%;
    background: var(--accent-blue);
  }
  .brand-name {
    font-family: "Michroma", sans-serif;
    font-size: 15px;
    color: var(--accent-blue);
    line-height: 1.35;
  }
</style>
</head>
<body>
  <section class="card card--contact">
    <h1 class="person-name">Daniel Hartley</h1>
    <p class="person-role">President</p>
    <ul class="contact-list">
      <li class="phone">P. 1300 862 317</li>
      <li>brightlanemotorparts@mailbox.example</li>
      <li>www.brightlanemotorparts.example</li>
    </ul>
    <div class="emboss-area" role="img" aria-label="Blind-embossed decorative mark"></div>
  </section>

  <section class="card card--brand">
    <div class="brand">
      <span class="brand-dot"></span>
      <span class="brand-name">Brightlane<br>Motor Parts</span>
    </div>
  </section>
</body>
</html>
```